Events professional capability flyer

I require a professional design for the attached document. I also attach a sample flyer to illustrate what I am wanting. It needs to be simple but eye catching and requires ALL the details on the word document. Please note the word document has been structured to keep the subject points together. This is very urgent & is required by tomorrow.

Target Market(s)

Event buyers

Industry/Entity Type

Events

Font styles to use
Other font styles liked:
• Professional & clear

Colors

Designer to choose colors to be used in the design.

Requirements
Must have
• - All the information on the word document
• - Simple eye catching design
Nice to have
• - Creative separation of sections
Should not have
• Pictures or background images / patterns

```html
<!DOCTYPE html>
<html lang="en">
<head>
<meta charset="utf-8">
<title>Crest Hoist – Capability Flyer</title>
<link rel="stylesheet" href="https://fonts.googleapis.com/css2?family=Montserrat:wght@700;800&family=Roboto:wght@400;500&display=swap">
<style>
:root{
  --teal:#2aa3c2;
  --teal-dark:#1b7a8e;
  --navy:#06243a;
  --ink:#1d2b3a;
  --body:#333b44;
  --grey-band:#5e5f62;
  --grey-strip:#c9c9c9;
  --icon-grey:#bfbfbf;
  --page:#d8d8d8;
  --white:#ffffff;
}
*{margin:0;padding:0;box-sizing:border-box}
html,body{width:703px;height:1200px;overflow:hidden;background:var(--page)}
body{position:relative;font-family:'Roboto',Arial,sans-serif}
.flyer{position:absolute;left:12px;top:120px;width:680px;height:961px;background:var(--white);box-shadow:0 6px 18px rgba(0,0,0,.25);overflow:hidden}
.abs{position:absolute}
.header{left:0;top:0;width:443px;height:158px;background:linear-gradient(180deg,#35b1d0 0%,#1f8aa0 100%)}
.header-strip{left:0;top:161px;width:443px;height:9px;background:var(--grey-strip)}
.title{left:30px;top:34px;font-family:'Montserrat',sans-serif;font-weight:800;font-size:50px;letter-spacing:.5px;color:var(--white);line-height:1}
.subtitle{left:31px;top:101px;font-size:21px;color:var(--white)}
.heading{left:31px;width:360px;font-family:'Montserrat',sans-serif;font-weight:700;font-size:12.3px;color:var(--ink);line-height:15px}
.copy{left:31px;width:350px;font-size:11.3px;line-height:13.6px;color:var(--body);text-align:justify}
.copy p+p{margin-top:13px}
.timeline{left:30px;top:695px;width:355px;height:90px}
.tl-label{position:absolute;font-size:11px;line-height:11.5px;color:var(--teal);text-align:center}
.founder-name{left:31px;top:815px;font-family:'Montserrat',sans-serif;font-weight:800;font-size:21px;color:var(--teal)}
.founder-role{left:31px;top:841px;font-size:12px;color:var(--ink)}
.contact{left:240px;font-size:11px;color:var(--ink);display:flex;align-items:center;gap:8px}
.contact svg{width:13px;height:13px}
.footer{left:0;top:897px;width:680px;height:64px;background:var(--grey-band)}
.footer-item{top:915px;font-family:'Roboto',sans-serif;font-weight:500;font-size:11px;line-height:13px;color:var(--white);display:flex;align-items:center;gap:9px}
.footer-item svg{width:14px;height:16px}
.panel{left:0;top:0;width:680px;height:961px}
.brand{left:482px;top:50px;display:flex;align-items:center;gap:10px;font-family:'Montserrat',sans-serif;font-weight:700;font-size:26px;color:var(--white);line-height:1}
.brand-dot{width:16px;height:16px;border-radius:50%;background:var(--white)}
.panel-title{left:475px;font-family:'Montserrat',sans-serif;font-weight:800;font-size:13.2px;line-height:14px;color:var(--teal)}
.group{left:502px}
.group h3{font-family:'Montserrat',sans-serif;font-weight:700;font-size:11.5px;color:var(--white);margin-bottom:5px}
.group li{list-style:none;font-size:10.5px;line-height:16px;color:var(--white);display:flex;align-items:center;gap:10px;padding-left:0}
.group li::before{content:"✓";display:inline-flex;align-items:center;justify-content:center;width:8px;height:8px;border:1px solid var(--teal);border-radius:50%;font-size:6px;color:var(--teal);line-height:1}
.icon-badge{width:68px;height:68px;margin-left:-34px;margin-top:-34px;border-radius:50%;background:var(--icon-grey);border:3px solid var(--white);display:flex;align-items:center;justify-content:center;box-shadow:0 1px 3px rgba(0,0,0,.2)}
.icon-badge svg{width:34px;height:34px}
</style>
</head>
<body>
<main class="flyer">

  <!-- Dark side panel and footer band -->
  <div class="abs footer"></div>
  <svg class="abs panel" viewBox="0 0 680 961" aria-hidden="true">
    <path d="M443 0H680V961H468Q443 925 443 860Z" fill="var(--navy)"/>
    <path d="M443 860Q443 925 468 961" fill="none" stroke="var(--white)" stroke-width="3"/>
  </svg>

  <!-- Header -->
  <div class="abs header"></div>
  <div class="abs header-strip"></div>
  <h1 class="abs title">CREST HOIST</h1>
  <p class="abs subtitle">Fan engagement / event theming</p>

  <!-- Main content -->
  <h2 class="abs heading" style="top:202px">COMPANY ELEVATOR PITCH</h2>
  <div class="abs copy" style="top:225px">
    <p>Crest Hoist is known for iconic brand displays, giant prop builds, experiential set builds, bespoke branding &amp; giant banner wraps internationally. From concept to design, build &amp; install Crest is the choice for the wow factor.</p>
  </div>

  <h2 class="abs heading" style="top:311px">WE ALSO HAVE CAPABILITIES WHICH INCLUDE</h2>
  <div class="abs copy" style="top:331px">
    <p>Branding, graphic design, large format print, site space marketing, signage and Rope Access maintenance works</p>
  </div>

  <h2 class="abs heading" style="top:393px">STATUS OF BUSINESS MATURITY AND OR<br>SUMMARY OF KEY REFERENCES/TESTIMONIALS</h2>
  <div class="abs copy" style="top:445px">
    <p>Crest Hoist are rapidly becoming the number 1 choice for fan engagement delivery ranging from stadium tifo banner reveals, immersive set builds, fan zones and include projects from a full-sized London tube replica build, iconic Thames Wheel’s 1 000m2 branded Chrome Rider rig.</p>
    <p>Crest Hoist has worked on a number of international sport events including the Global Summer Games, football world cup, rugby world cup and more. Our experience includes iconic structure dressing such as the Thames Wheel, Spree Tower, Civic Hall, Gulf Trade Tower to name a few and major sport venues across more than 8 countries.</p>
    <p>Our Industrial arm delivers top quality rope access services to include construction, roof works, maintenance, screen installations, cabling, painting, corrosion repair, safety systems, signage</p>
  </div>

  <!-- Process timeline -->
  <div class="abs timeline">
    <svg class="abs" style="left:0;top:0" width="355" height="90" viewBox="0 0 355 90" aria-hidden="true">
      <g stroke="var(--ink)" stroke-width="1.5" fill="none">
        <line x1="12" y1="50" x2="328" y2="50"/>
        <line x1="12" y1="36" x2="12" y2="64"/>
        <line x1="328" y1="36" x2="328" y2="50"/>
        <line x1="96" y1="38" x2="96" y2="50"/>
        <line x1="187" y1="38" x2="187" y2="50"/>
        <line x1="34" y1="50" x2="34" y2="62"/>
        <line x1="120" y1="50" x2="120" y2="62"/>
        <line x1="236" y1="50" x2="236" y2="62"/>
      </g>
    </svg>
    <span class="tl-label" style="left:0;top:14px">Concept</span>
    <span class="tl-label" style="left:76px;top:14px">Design</span>
    <span class="tl-label" style="left:152px;top:6px;width:72px">International logistics</span>
    <span class="tl-label" style="left:280px;top:8px;width:75px">Full project management</span>
    <span class="tl-label" style="left:14px;top:64px;width:42px">Survey &amp; proposal</span>
    <span class="tl-label" style="left:92px;top:64px">Build / print</span>
    <span class="tl-label" style="left:200px;top:64px;width:72px">Installation &amp; rigging</span>
  </div>

  <!-- Contact -->
  <p class="abs founder-name">MARTIN HALE*</p>
  <p class="abs founder-role">Founder &amp; Managing Director *</p>
  <p class="abs contact" style="top:822px">
    <svg viewBox="0 0 16 16" aria-hidden="true"><path d="M4 1l2.5 3-1.5 1.6c.9 2 2.4 3.5 4.4 4.4L11 8.5 14 11l-1.6 2.8C7 13.4 2.6 9 2.2 3.6z" fill="var(--teal)"/></svg>
    +44 7700 900418
  </p>
  <p class="abs contact" style="top:841px">
    <svg viewBox="0 0 16 16" aria-hidden="true"><rect x="1" y="3.5" width="14" height="9.5" fill="var(--teal)"/><path d="M1 3.5l7 5.5 7-5.5" fill="none" stroke="var(--white)" stroke-width="1.2"/></svg>
    martin@crest-hoist.com
  </p>

  <!-- Footer -->
  <p class="abs footer-item" style="left:34px;top:922px">
    <svg viewBox="0 0 16 16" aria-hidden="true"><circle cx="8" cy="8" r="7" fill="var(--teal)"/><path d="M4 6c2 0 2 2 4 2s1 3 0 4M9 2c0 2 3 2 4 4" fill="none" stroke="var(--grey-band)" stroke-width="1.3"/></svg>
    WWW.CREST-HOIST.COM
  </p>
  <p class="abs footer-item" style="left:231px">
    <svg viewBox="0 0 14 18" aria-hidden="true"><path d="M7 1a5.5 5.5 0 0 1 5.5 5.5C12.5 11 7 16 7 16S1.5 11 1.5 6.5A5.5 5.5 0 0 1 7 1z" fill="var(--teal)"/><circle cx="7" cy="6.5" r="2" fill="var(--grey-band)"/><ellipse cx="7" cy="16.5" rx="4" ry="1" fill="var(--teal)"/></svg>
    <span>Unit C2 Harbour Point Meadow Lane<br>London UK E9 4XY</span>
  </p>

  <!-- Side panel content -->
  <div class="abs brand"><span class="brand-dot"></span>Crest Hoist</div>

  <h2 class="abs panel-title" style="top:163px">WE DELIVER 3 CENTRAL<br>PROPOSITIONS</h2>

  <div class="abs icon-badge" style="left:443px;top:258px">
    <svg viewBox="0 0 34 34" aria-hidden="true"><path d="M13 11a7 7 0 1 0 0 12" fill="none" stroke="#555" stroke-width="4"/><rect x="18" y="8" width="5" height="5" fill="#555"/><rect x="25" y="14" width="5" height="5" fill="#555"/><rect x="18" y="20" width="5" height="5" fill="#555"/></svg>
  </div>
  <section class="abs group" style="top:224px">
    <h3>FAN ENGAGEMENT</h3>
    <ul><li>Fan zones</li><li>Creative branding</li><li>Immersive builds</li></ul>
  </section>

  <div class="abs icon-badge" style="left:443px;top:357px">
    <svg viewBox="0 0 34 34" aria-hidden="true"><circle cx="14" cy="15" r="8" fill="none" stroke="#555" stroke-width="4" stroke-dasharray="4 2.3"/><circle cx="14" cy="15" r="3" fill="#555"/><circle cx="24" cy="24" r="5" fill="none" stroke="#555" stroke-width="3" stroke-dasharray="3 2"/></svg>
  </div>
  <section class="abs group" style="top:321px">
    <h3>THEMING / SET BUILDS</h3>
    <ul><li>Set Builds</li><li>3D props</li><li>Scene design &amp; build</li></ul>
  </section>

  <div class="abs icon-badge" style="left:443px;top:455px">
    <svg viewBox="0 0 34 34" aria-hidden="true"><g fill="none" stroke="#555" stroke-width="3"><rect x="6" y="6" width="22" height="22"/><path d="M6 6l8 8M28 6l-8 8M6 28l8-8M28 28l-8-8"/></g></svg>
  </div>
  <section class="abs group" style="top:422px">
    <h3>RIGGING</h3>
    <ul><li>Tifo banner reveals</li><li>Suspended props</li><li>Giant wraps</li></ul>
  </section>

  <h2 class="abs panel-title" style="top:530px">OUR TYPICAL<br>CLIENTS INCLUDE</h2>

  <div class="abs icon-badge" style="left:443px;top:622px">
    <svg viewBox="0 0 34 34" aria-hidden="true"><g fill="none" stroke="#555" stroke-width="2.5"><rect x="5" y="8" width="24" height="21" rx="2"/><path d="M5 13h24M11 4v6M23 4v6M12 21l4 4 7-8"/></g></svg>
  </div>
  <section class="abs group" style="top:586px">
    <h3>EVENT ORGANISERS</h3>
    <ul><li>Production companies</li><li>Sports Competitions</li><li>Concert Organisers</li></ul>
  </section>

  <div class="abs icon-badge" style="left:443px;top:720px">
    <svg viewBox="0 0 34 34" aria-hidden="true"><g fill="#555"><rect x="5" y="12" width="24" height="16" rx="2"/><rect x="12" y="7" width="10" height="6" rx="1" fill="none" stroke="#555" stroke-width="2.5"/></g><path d="M5 19h24" stroke="var(--icon-grey)" stroke-width="2"/></svg>
  </div>
  <section class="abs group" style="top:689px">
    <h3>COMMERCIAL CLIENTS</h3>
    <ul><li>Sporting brands</li><li>Construction companies</li><li>Retail</li></ul>
  </section>

  <div class="abs icon-badge" style="left:443px;top:828px">
    <svg viewBox="0 0 34 34" aria-hidden="true"><path d="M3 14Q17 6 31 14V24H3Z" fill="#555"/><path d="M7 17v5M11 16v6M15 15v7M19 15v7M23 16v6M27 17v5" stroke="var(--icon-grey)" stroke-width="1.5"/></svg>
  </div>
  <section class="abs group" style="top:795px">
    <h3>VENUES</h3>
    <ul><li>Stadiums</li><li>Race tracks</li><li>Public spaces / buildings</li></ul>
  </section>

</main>
</body>
</html>
```